Box for baby swaddle blankets.

Hi there!

I'd like you to make a packaging design for the box of my muslin swaddle blankets which I'll be selling on Pindlewick.com. I want the product to be the perfect baby shower gift! Most of the packages of my competitors are made by the manufacturing company, so they're pretty simple and similar to each other, I'd like you to make a unique design for me. I included a detailed description about the parameters in the "must haves" section. If you have any questions or suggestions, please message me.

Target Market(s)

Pindlewick.com

Industry/Entity Type

Baby Care

Colors

Designer to choose colors to be used in the design.

Requirements
Must have
• 1. Most of my competitors use pretty basic packaging, so I'd like stand out with my box. I was thinking about putting my logo at the bottom of the front side, and make heart-shaped cuts above the elephant's trunk, which would allow buyers to see the fabric and the pattern of the blankets. You can remove the heart from my logo since I think it wouldn't look good with the cuts above it. Tell me what you think about this, I'm also open for other ideas for the front as well as long as it makes the packaging unique and gives the buyers a peek of the blankets.
• I attached some examples of cuts I've seen on packages.
• 2. I'd like you to use the title BABY SWADDLE BLANKETS and my logo on the front. The package contains 3 blankets are made from organic muslin cotton with 47x47 inch size, you could include this also in the front if you can find a good way for it .
• Also, I'd like to have a stamp of 100% ORGANIC COTTON in one corner.
• The package will contain a bonus baby bandana bib, so please put a BANDANA BIB GIFT INSIDE! object with an arrow pointing in the box in the front.
• 3. For the sides, one of them should show the different ways you can use these blankets, with illustrations. I'll attach some examples for this (I like the pictogram-type illustration on img1 better) . You can add my logo for the top side. You can try to add the words "BREATHABLE" "EXTRA SOFT" "LARGE SIZE" "100% ORGANIC COTTON" on the remaining side(s) if it would look good in your opinion.
• 4. For the back, I'd like you to add a 4-step instruction about how to swaddle the baby with the blankets. Since almost all of competitors use the same images, I'd like you to design new ones, make it playful and baby-friendly :) I'll attach some examples for these instructions as well.. The bottom of the back should contain the text "Made with care in China, designed with love in the United States" and a place for the barcode.
• 4. The box should be the size of 21*22*8 in centimeters.
• If you have any questions or suggestions for the design, please message me.
Nice to have
• If you have any other ideas or suggestions about the design, feel free to contact me.

```html
<!DOCTYPE html>
<html lang="en">
<head>
<meta charset="utf-8">
<title>Baby Swaddle Blankets – Box Fronts</title>
<link rel="stylesheet" href="https://fonts.googleapis.com/css2?family=Dancing+Script:wght@500;700&family=Arimo:wght@400;700&display=swap">
<style>
  :root {
    --backdrop: #352d2b;
    --board: #ffffff;
    --pale: #eefbfb;
    --crimson: #e8104f;
    --magenta: #e513a6;
    --navy-script: #2a4f8f;
  }
  * { margin: 0; padding: 0; box-sizing: border-box; }
  html, body { width: 1200px; height: 800px; overflow: hidden; }
  body { background: var(--backdrop); position: relative; font-family: "Arimo", Arial, sans-serif; }

  .box-front {
    position: absolute;
    top: 118px;
    width: 561px;
    height: 536px;
    background: var(--board);
    box-shadow: 6px 6px 8px rgba(0,0,0,.55);
  }
  .box-front svg { display: block; width: 100%; height: 100%; }
  .box-front--teal { left: 25px;
    --stripe: #3f8696; --stripe-gap: #eefafa; --heart-edge: #9fb9bd;
    --banner: #eefafd; --banner-edge: #9cc9d6; --tail: #d7f0d9;
    --title: #1f73c8; --count: var(--crimson); --size-text: #3c6ccc;
    --gift: var(--crimson); --frame: #ffffff; --brand: #6cc5e6; }
  .box-front--pink { left: 618px;
    --stripe: #f1a3b6; --stripe-gap: #f1fbfb; --heart-edge: #e7a9bb;
    --banner: #fdf2fa; --banner-edge: #e6a9c4; --tail: #e9def0;
    --title: #22bfc4; --count: var(--magenta); --size-text: #5bb4c9;
    --gift: var(--magenta); --frame: #f3b4c4; --brand: #6cc5e6; }

  .stripe-gap { fill: var(--stripe-gap); }
  .stripe { fill: var(--stripe); }
  .corner-fold { fill: var(--pale); }
  .organic-stamp { fill: #ffffff; stroke: #2f8a3a; stroke-width: 3; }
  .organic-stamp__ring { fill: none; stroke: #2f8a3a; stroke-width: 1.5; }
  .heart-window { stroke: var(--heart-edge); stroke-width: 3; }
  .banner { fill: var(--banner); stroke: var(--banner-edge); stroke-width: 2; }
  .banner-tail { fill: var(--tail); stroke: var(--banner-edge); stroke-width: 1.5; }
  .title { font-family: "Dancing Script", cursive; font-weight: 700; font-size: 56px; fill: var(--title); }
  .subtitle { font-family: "Dancing Script", cursive; font-weight: 500; font-size: 18px; fill: var(--navy-script); }
  .info-band { fill: var(--pale); }
  .frame-line { fill: none; stroke: var(--frame); stroke-width: 3; }
  .count { font-family: "Arimo", Arial, sans-serif; font-weight: 700; font-size: 46px; fill: var(--count); }
  .size-note { font-family: "Arimo", Arial, sans-serif; font-size: 19px; fill: var(--size-text); }
  .brand-name { font-family: "Dancing Script", cursive; font-weight: 500; font-size: 44px; fill: var(--brand); }
  .brand-dot { fill: var(--brand); }
  .gift-text { font-family: "Arimo", Arial, sans-serif; font-size: 18px; fill: #2a62c9; }
  .gift-tag { fill: var(--gift); }
  .gift-tag__text { font-family: "Arimo", Arial, sans-serif; font-style: italic; font-size: 18px; fill: #ffffff; }
  .gift-arrow { fill: var(--gift); }
</style>
</head>
<body>

<!-- Teal edition -->
<div class="box-front box-front--teal">
  <svg viewBox="0 0 701 669" xmlns="http://www.w3.org/2000/svg">
    <defs>
      <pattern id="stripes-teal" patternUnits="userSpaceOnUse" width="67" height="20" x="15">
        <rect class="stripe" x="0" y="0" width="33" height="20"/>
      </pattern>
      <linearGradient id="fabric-teal" x1="0" y1="0" x2="1" y2="1">
        <stop offset="0" stop-color="#e9eeec"/>
        <stop offset=".35" stop-color="#dfe9e6"/>
        <stop offset=".7" stop-color="#d3eef0"/>
        <stop offset="1" stop-color="#e7efee"/>
      </linearGradient>
    </defs>
    <rect class="stripe-gap" x="15" y="15" width="674" height="523"/>
    <rect x="15" y="15" width="674" height="523" fill="url(#stripes-teal)"/>
    <polygon class="corner-fold" points="15,15 125,15 15,145"/>
    <circle class="organic-stamp" cx="51" cy="49" r="26"/>
    <circle class="organic-stamp__ring" cx="51" cy="49" r="20"/>

    <path class="heart-window" fill="url(#fabric-teal)" role="img" aria-label="Peek at the folded muslin blankets with whale, tree and wave prints"
      d="M347,145 C330,115 290,108 240,117 C150,130 103,200 116,272 C133,362 262,432 347,520 C432,432 561,362 578,272 C591,200 544,130 454,117 C404,108 364,115 347,145 Z"/>

    <path class="banner-tail" d="M92,332 L24,356 L66,382 L36,428 L128,404 Z"/>
    <path class="banner-tail" d="M575,308 L676,360 L630,386 L650,432 L560,400 Z"/>
    <path class="banner" d="M60,298 Q330,170 575,290 L570,350 Q330,245 72,360 Z"/>
    <path id="title-arc-teal" d="M110,316 Q330,215 570,312" fill="none"/>
    <path id="sub-arc-teal" d="M230,328 Q340,292 470,322" fill="none"/>
    <text class="title"><textPath href="#title-arc-teal" startOffset="50%" text-anchor="middle">Baby Swaddle Blankets</textPath></text>
    <text class="subtitle"><textPath href="#sub-arc-teal" startOffset="50%" text-anchor="middle">made from organic muslin cotton</textPath></text>

    <rect class="info-band" x="15" y="538" width="674" height="107"/>
    <rect x="15" y="645" width="674" height="12" fill="url(#stripes-teal)"/>
    <text class="count" x="104" y="595">3</text>
    <text class="size-note" x="13" y="629">Blankets 47x47 inch size</text>

    <circle class="brand-dot" cx="358" cy="562" r="7"/>
    <text class="brand-name" x="358" y="628" text-anchor="middle">Snugglory</text>

    <text class="gift-text" x="532" y="574">BANDANA</text>
    <text class="gift-text" x="532" y="598">BIB</text>
    <rect class="gift-tag" x="563" y="580" width="66" height="23"/>
    <text class="gift-tag__text" x="568" y="598">GIFT</text>
    <text class="gift-text" x="532" y="622">INSIDE!</text>
    <polygon class="gift-arrow" points="631,559 679,590 631,622"/>
  </svg>
</div>

<!-- Pink edition -->
<div class="box-front box-front--pink">
  <svg viewBox="0 0 701 669" xmlns="http://www.w3.org/2000/svg">
    <defs>
      <pattern id="stripes-pink" patternUnits="userSpaceOnUse" width="67" height="20" x="15">
        <rect class="stripe" x="0" y="0" width="33" height="20"/>
      </pattern>
      <linearGradient id="fabric-pink" x1="0" y1="0" x2="1" y2="1">
        <stop offset="0" stop-color="#e9eeec"/>
        <stop offset=".35" stop-color="#dfe9e6"/>
        <stop offset=".7" stop-color="#d3eef0"/>
        <stop offset="1" stop-color="#e7efee"/>
      </linearGradient>
    </defs>
    <rect class="stripe-gap" x="15" y="15" width="674" height="523"/>
    <rect x="15" y="15" width="674" height="523" fill="url(#stripes-pink)"/>
    <polygon class="corner-fold" points="15,15 125,15 15,145"/>
    <circle class="organic-stamp" cx="51" cy="49" r="26"/>
    <circle class="organic-stamp__ring" cx="51" cy="49" r="20"/>

    <path class="heart-window" fill="url(#fabric-pink)" role="img" aria-label="Peek at the folded muslin blankets with whale, tree and wave prints"
      d="M347,145 C330,115 290,108 240,117 C150,130 103,200 116,272 C133,362 262,432 347,520 C432,432 561,362 578,272 C591,200 544,130 454,117 C404,108 364,115 347,145 Z"/>

    <path class="banner-tail" d="M92,332 L24,356 L66,382 L36,428 L128,404 Z"/>
    <path class="banner-tail" d="M575,308 L676,360 L630,386 L650,432 L560,400 Z"/>
    <path class="banner" d="M60,298 Q330,170 575,290 L570,350 Q330,245 72,360 Z"/>
    <path id="title-arc-pink" d="M110,316 Q330,215 570,312" fill="none"/>
    <path id="sub-arc-pink" d="M230,328 Q340,292 470,322" fill="none"/>
    <text class="title"><textPath href="#title-arc-pink" startOffset="50%" text-anchor="middle">Baby Swaddle Blankets</textPath></text>
    <text class="subtitle"><textPath href="#sub-arc-pink" startOffset="50%" text-anchor="middle">made from organic muslin cotton</textPath></text>

    <rect class="info-band" x="15" y="538" width="674" height="107"/>
    <rect x="15" y="645" width="674" height="12" fill="url(#stripes-pink)"/>
    <rect class="frame-line" x="14" y="14" width="676" height="644"/>
    <text class="count" x="104" y="595">3</text>
    <text class="size-note" x="18" y="629">Blankets 47x47 inch size</text>

    <circle class="brand-dot" cx="358" cy="562" r="7"/>
    <text class="brand-name" x="358" y="628" text-anchor="middle">Snugglory</text>

    <text class="gift-text" x="532" y="574">BANDANA</text>
    <text class="gift-text" x="532" y="598">BIB</text>
    <rect class="gift-tag" x="563" y="580" width="66" height="23"/>
    <text class="gift-tag__text" x="568" y="598">GIFT</text>
    <text class="gift-text" x="532" y="622">INSIDE!</text>
    <polygon class="gift-arrow" points="631,559 679,590 631,622"/>
  </svg>
</div>

</body>
</html>
```